Business cards for law firm with global theme

I'd like business cards with contact info for two offices. They should include the colors and font of the new logo design, which is a stylized globe with an "F" in it. The feel should be very modern and professional.

```html
<!DOCTYPE html>
<html lang="en">
<head>
<meta charset="utf-8">
<title>Vantara Law – Business Card</title>
<link href="https://fonts.googleapis.com/css2?family=Lato:wght@400;700;900&display=swap" rel="stylesheet">
<style>
  :root {
    --navy: #173f6f;
    --sky: #27a9e1;
    --ink: #4a4a4a;
    --paper: #ffffff;
    --backdrop: #eeeeec;
    --pattern-base: #163f6e;
    --pattern-deep: #12345e;
    --pattern-silver: #c9cfdf;
    --pattern-mid: #6f7fa6;
  }
  * { margin: 0; padding: 0; box-sizing: border-box; }
  html, body {
    width: 1200px; height: 1200px; overflow: hidden;
    background: var(--backdrop);
    font-family: "Lato", Arial, sans-serif;
  }
  .card {
    position: absolute;
    left: 153px;
    width: 894px;
    height: 515px;
    box-shadow: 0 8px 24px rgba(0,0,0,0.18);
  }
  .card--front { top: 55px; background: var(--paper); overflow: hidden; }
  .card--back { top: 629px; overflow: hidden; }

  .brand {
    position: absolute; left: 40px; top: 141px; width: 400px;
    display: flex; flex-direction: column; align-items: center;
  }
  .brand__mark {
    width: 128px; height: 128px; border-radius: 50%;
    background: var(--navy);
  }
  .brand__name {
    margin-top: 24px;
    font-weight: 900; font-size: 44px; letter-spacing: 1px;
    color: var(--navy); white-space: nowrap;
  }

  .divider {
    position: absolute; left: 447px; top: 143px;
    width: 2px; height: 231px; background: var(--sky);
  }

  .contact {
    position: absolute; left: 495px; top: 137px;
    color: var(--ink);
  }
  .contact__name {
    font-weight: 700; font-size: 31px; line-height: 1.1; letter-spacing: 0.2px;
    color: var(--navy);
  }
  .contact__name span { color: var(--sky); }
  .contact__title { font-size: 21px; margin-top: 2px; }
  .contact__address { font-size: 21px; line-height: 31px; margin-top: 14px; }
  .contact__list { list-style: none; margin-top: 12px; }
  .contact__item {
    display: flex; align-items: center; gap: 10px;
    font-size: 21px; line-height: 31px;
  }
  .contact__icon { width: 19px; height: 19px; flex: none; }

  .band { position: absolute; left: 0; bottom: 0; width: 894px; height: 24px; }

  .pattern-fill {
    width: 100%; height: 100%;
    background:
      linear-gradient(120deg,
        rgba(201,207,223,0.0) 0%,
        rgba(201,207,223,0.55) 14%,
        rgba(111,127,166,0.25) 26%,
        rgba(18,52,94,0.0) 36%,
        rgba(201,207,223,0.0) 44%,
        rgba(201,207,223,0.6) 56%,
        rgba(111,127,166,0.25) 68%,
        rgba(18,52,94,0.0) 78%,
        rgba(201,207,223,0.45) 92%,
        rgba(201,207,223,0.2) 100%),
      var(--pattern-base);
  }
</style>
</head>
<body>
  <section class="card card--front">
    <div class="brand">
      <div class="brand__mark"></div>
      <div class="brand__name">VANTARA LAW</div>
    </div>

    <div class="divider"></div>

    <div class="contact">
      <h1 class="contact__name">DANIEL <span>REYES</span></h1>
      <p class="contact__title">President</p>
      <p class="contact__address">1820 Harbor Lane, Millbrook<br>NC 2, United States</p>
      <ul class="contact__list">
        <li class="contact__item">
          <svg class="contact__icon" viewBox="0 0 24 24"><path fill="#27a9e1" d="M6.6 10.8a15 15 0 0 0 6.6 6.6l2.2-2.2c.3-.3.7-.4 1-.2 1.1.4 2.3.6 3.6.6.6 0 1 .4 1 1V20c0 .6-.4 1-1 1C10.6 21 3 13.4 3 4c0-.6.4-1 1-1h3.5c.6 0 1 .4 1 1 0 1.3.2 2.5.6 3.6.1.3 0 .7-.2 1z"/><path fill="none" stroke="#27a9e1" stroke-width="1.8" d="M14 3a7 7 0 0 1 7 7M14 6.5a3.5 3.5 0 0 1 3.5 3.5"/></svg>
          000-000-000-000
        </li>
        <li class="contact__item">
          <svg class="contact__icon" viewBox="0 0 24 24"><rect x="2" y="5" width="20" height="14" fill="#27a9e1"/><path d="M2 5l10 8 10-8M2 19l7-7M22 19l-7-7" fill="none" stroke="#fff" stroke-width="1.6"/></svg>
          info@websitename.com
        </li>
        <li class="contact__item">
          <svg class="contact__icon" viewBox="0 0 24 24" fill="none" stroke="#27a9e1" stroke-width="1.8"><circle cx="12" cy="12" r="10"/><ellipse cx="12" cy="12" rx="4.5" ry="10"/><path d="M2 12h20M4 7h16M4 17h16"/></svg>
          www.websitename.com
        </li>
      </ul>
    </div>

    <svg class="band" viewBox="0 0 894 24" preserveAspectRatio="none">
      <polygon points="0,0 440,0 416,24 0,24" fill="#173f6f"/>
      <polygon points="449,0 894,0 894,24 425,24" fill="#27a9e1"/>
    </svg>
  </section>

  <section class="card card--back">
    <div class="pattern-fill" role="img" aria-label="Repeating pattern of the firm's globe symbol in rows, shading from navy to silver-white, on a navy field"></div>
  </section>
</body>
</html>
```